Survey App for phone users trying a new phone with Dual connectivity

Survey App Brief<br/>Design For an Android Survey App for users' feedback on Call, SMS, Data and Streaming Experience on their Mobile phones.<br/><br/>Purpose of the App<br/>To ensure that the user's experience is not impacted by the network switching between two network on the special mobile phones they newly started using.<br/><br/>App Requirements:<br/>First screen: The registration screen, where the user needs to enter the following:<br/>Name: text box<br/>Phone Number: text box<br/>Group Number : <br/><br/>An information text:<br/>By Registering I agree to participate in the Survey.<br/><br/>Register: Button<br/><br/>Start Screen - Survey screens (next time user open the App this will be the first screen):<br/>We need feedback for 4 indicators:<br/>Call Experience<br/>SMS Experience<br/>Data Experience<br/>Streaming Experience<br/><br/>Each Experience can be in the form of a questionnaire or Satisfied/ Somewhat Satisfied / Extremely Satisfied form with radio buttons or on a scale of 1 to 5. We need to ensure that the format used is very professional.<br/><br/>An optional text box for the user to enter the comment in a free format.<br/><br/>This can be done in 4 different screens or in one single screen if it does not give a clumsy look.<br/><br/>A Send button at the end to submit the Survey.<br/><br/>We need a burger menu at the top left corner of this screen, which when expanded will provide 5 options:<br/>Edit User Profile<br/>Survey interval Timer<br/>FAQ<br/>Exit<br/>About<br/><br/><br/>Please ensure that the app is simple, friendly, lively and professional at the same time so that it ignites an interest in the user to use the app.<br/>Use Logo as appropriate.
Industry/Entity Type
Telecommunications
Colors
Designer to choose colors to be used in the design.
Look and feel
Each slider illustrates characteristics of the customer's brand and the style your logo design should communicate.

```html
<!DOCTYPE html>
<html lang="en">
<head>
<meta charset="utf-8">
<title>Survey App – Screens</title>
<link href="https://fonts.googleapis.com/css2?family=Poppins:wght@400;500;600&family=Montserrat:wght@600&display=swap" rel="stylesheet">
<style>
  :root {
    --ink: #1c1c1c;
    --muted: #8a8a8a;
    --line: #ececec;
    --tint: #d3e9f6;
    --accent: #5cc8f0;
    --page: #ffffff;
    --shade: #f6f6f6;
  }
  * { box-sizing: border-box; margin: 0; padding: 0; }
  html, body { width: 951px; height: 1200px; overflow: hidden; background: var(--page); }
  body { position: relative; font-family: "Poppins", sans-serif; color: var(--ink); }

  .screen {
    position: absolute; width: 186px; height: 404px;
    background: var(--page); border: 1px solid var(--line); border-radius: 14px; overflow: hidden;
  }
  .screen--register { left: 214px; top: 60px; }
  .screen--survey { left: 557px; top: 60px; }
  .screen--experience { left: 213px; top: 628px; }
  .screen--menu { left: 556px; top: 628px; }

  .caption {
    position: absolute; width: 186px; text-align: center;
    font-family: "Montserrat", sans-serif; font-weight: 600; font-size: 11px; letter-spacing: 1.4px;
  }

  .abs { position: absolute; }

  .brand { display: flex; align-items: center; gap: 4px; font-size: 6px; font-weight: 500; color: var(--muted); letter-spacing: .5px; text-transform: uppercase; }
  .brand__dot { width: 9px; height: 9px; border-radius: 50%; background: var(--accent); }

  /* registration */
  .headline { left: 8px; top: 80px; font-size: 16px; line-height: 19px; font-weight: 400; }
  .headline strong { font-weight: 600; display: block; }
  .form-card { left: 20px; top: 143px; width: 146px; height: 206px; border: 1px solid var(--line); border-radius: 6px; }
  .field {
    position: absolute; left: 14px; width: 118px; height: 25px;
    border: 1px solid var(--line); border-radius: 5px;
    font-size: 7px; color: var(--muted); padding: 0 7px; display: flex; align-items: center;
  }
  .agree { position: absolute; left: 14px; top: 130px; display: flex; align-items: center; gap: 4px; font-size: 5.5px; color: var(--muted); }
  .agree__box { width: 7px; height: 7px; border: 1px solid #b9c8d4; border-radius: 1.5px; display: flex; align-items: center; justify-content: center; }
  .btn {
    position: absolute; width: 120px; height: 30px; border-radius: 7px;
    background: var(--ink); color: #fff; font-size: 7.5px; font-weight: 600;
    display: flex; align-items: center; justify-content: center;
  }

  /* survey */
  .icon-btn { width: 20px; height: 18px; border-radius: 5px; background: var(--tint); display: flex; align-items: center; justify-content: center; }
  .greeting { right: 8px; top: 22px; text-align: right; font-size: 8px; line-height: 12px; }
  .greeting strong { font-weight: 500; display: block; }
  .lead { left: 8px; font-size: 8px; }
  .lead strong { font-weight: 500; }
  .tile {
    position: absolute; width: 81px; height: 77px; border: 1px solid var(--line); border-radius: 5px;
    padding: 16px 8px 0;
  }
  .tile--active { background: var(--tint); border-color: var(--tint); }
  .tile__label { position: absolute; left: 8px; bottom: 12px; font-size: 7px; white-space: nowrap; }
  .tile__label strong { font-weight: 500; }

  /* experience */
  .title { left: 0; width: 186px; top: 24px; text-align: center; font-size: 9.5px; }
  .title strong { font-weight: 500; }
  .option {
    position: absolute; left: 9px; width: 169px; height: 33px; border: 1px solid var(--line); border-radius: 4px;
    display: flex; align-items: center; gap: 10px; padding-left: 9px; font-size: 8px; font-weight: 500;
  }
  .option--active { background: var(--tint); border-color: var(--tint); }
  .option__mark { width: 15px; height: 15px; border: 1.2px solid var(--ink); border-radius: 50%; }
  .comment { left: 9px; top: 285px; width: 169px; height: 44px; border: 1px solid var(--line); border-radius: 4px; padding: 6px; font-size: 6.5px; color: var(--muted); }

  /* side menu */
  .drawer { left: 0; top: 0; width: 150px; height: 404px; background: var(--page); border-right: 1px solid var(--line); }
  .backdrop { left: 150px; top: 0; width: 36px; height: 404px; background: var(--page); }
  .backdrop__text { position: absolute; font-size: 8px; color: #777; filter: blur(1.6px); white-space: nowrap; }
  .menu-item { position: absolute; left: 18px; width: 114px; height: 24px; padding-left: 8px; display: flex; align-items: center; font-size: 8px; color: #555; }
  .menu-item--active { background: var(--tint); border-radius: 12px; color: var(--ink); }
</style>
</head>
<body>

<!-- Registration -->
<section class="screen screen--register">
  <div class="abs brand" style="left:0;width:186px;top:28px;justify-content:center;">
    <span class="brand__dot"></span>Meridian Labs
  </div>
  <h1 class="abs headline">Lets start with <strong>register!</strong></h1>
  <div class="abs form-card">
    <div class="field" style="top:18px;">Name</div>
    <div class="field" style="top:55px;">Phone</div>
    <div class="field" style="top:93px;">Group Number</div>
    <div class="agree">
      <span class="agree__box"><svg width="5" height="5" viewBox="0 0 10 10"><path d="M1.5 5.5l2.5 2.5 4.5-6" fill="none" stroke="#2a5d86" stroke-width="1.8"/></svg></span>
      I agree to participate in the survey
    </div>
    <div class="btn" style="left:13px;top:158px;">REGISTER</div>
  </div>
</section>
<div class="caption" style="left:214px;top:503px;">REGISTERATION</div>

<!-- Survey -->
<section class="screen screen--survey">
  <div class="abs icon-btn" style="left:8px;top:23px;">
    <svg width="10" height="8" viewBox="0 0 10 8"><path d="M0 1h10M0 4h6M0 7h10" stroke="#1c1c1c" stroke-width="1"/></svg>
  </div>
  <div class="abs brand" style="left:60px;width:66px;top:29px;justify-content:center;">Meridian</div>
  <div class="abs greeting">Hello<strong>Daniel!</strong></div>
  <p class="abs lead" style="top:111px;">Lets Share Your <strong>Experience</strong></p>

  <div class="tile tile--active" style="left:8px;top:132px;">
    <svg width="18" height="18" viewBox="0 0 24 24"><path d="M6.6 10.8a15 15 0 0 0 6.6 6.6l2.2-2.2a1 1 0 0 1 1-.25 11.4 11.4 0 0 0 3.6.57 1 1 0 0 1 1 1V20a1 1 0 0 1-1 1A17 17 0 0 1 3 4a1 1 0 0 1 1-1h3.5a1 1 0 0 1 1 1c0 1.25.2 2.45.57 3.6a1 1 0 0 1-.25 1z" fill="#5cc8f0"/></svg>
    <span class="tile__label">Call <strong>Experience</strong></span>
  </div>
  <div class="tile" style="left:97px;top:132px;">
    <svg width="18" height="18" viewBox="0 0 24 24"><circle cx="9.5" cy="9.5" r="7.5" fill="#5cc8f0"/><path d="M21 11a6.5 6.5 0 0 1-3 10.5l2 1-5-1A7 7 0 0 1 10.5 18" fill="none" stroke="#5cc8f0" stroke-width="1.6"/></svg>
    <span class="tile__label">SMS <strong>Experience</strong></span>
  </div>
  <div class="tile" style="left:8px;top:218px;">
    <svg width="18" height="18" viewBox="0 0 24 24"><circle cx="7" cy="7" r="5" fill="none" stroke="#5cc8f0" stroke-width="1.2" stroke-dasharray="1.5 1.2"/><rect x="14" y="12" width="6" height="9" rx="1" fill="#5cc8f0"/><path d="M12 8h6v3" fill="none" stroke="#5cc8f0" stroke-width="1.2"/></svg>
    <span class="tile__label">Data <strong>Experience</strong></span>
  </div>
  <div class="tile" style="left:97px;top:218px;">
    <svg width="18" height="18" viewBox="0 0 24 24"><circle cx="12" cy="12" r="9" fill="none" stroke="#5cc8f0" stroke-width="1.4" stroke-dasharray="2 1.6"/><path d="M10 8.5v7l5.5-3.5z" fill="#5cc8f0"/></svg>
    <span class="tile__label">Stream <strong>Experience</strong></span>
  </div>
</section>
<div class="caption" style="left:557px;top:503px;">SURVEY</div>

<!-- Experience -->
<section class="screen screen--experience">
  <div class="abs icon-btn" style="left:9px;top:23px;width:19px;height:17px;">
    <svg width="9" height="8" viewBox="0 0 10 8"><path d="M9 4H1.5M4.5 1 1.2 4l3.3 3" fill="none" stroke="#1c1c1c" stroke-width="1"/></svg>
  </div>
  <h2 class="abs title" style="font-weight:400;">Call <strong>Experience</strong></h2>
  <p class="abs lead" style="top:76px;left:9px;">How you rate our calling <strong>experience?</strong></p>
  <div class="option option--active" style="top:110px;"><span class="option__mark"></span>Extremely Satisfied</div>
  <div class="option" style="top:153px;"><span class="option__mark"></span>Satisfied</div>
  <div class="option" style="top:197px;"><span class="option__mark"></span>Some What</div>
  <div class="option" style="top:241px;"><span class="option__mark"></span>Not Satisfied</div>
  <div class="abs comment">Write Here...</div>
  <div class="btn" style="left:33px;top:349px;">SEND</div>
</section>
<div class="caption" style="left:213px;top:1072px;">EXPERIENCE</div>

<!-- Side menu -->
<section class="screen screen--menu">
  <div class="abs backdrop">
    <span class="backdrop__text" style="left:8px;top:24px;">Hello</span>
    <span class="backdrop__text" style="left:0;top:36px;">Daniel!</span>
  </div>
  <nav class="abs drawer">
    <div class="abs brand" style="left:0;width:150px;top:50px;justify-content:center;">
      <span class="brand__dot"></span>Meridian Labs
    </div>
    <div class="menu-item menu-item--active" style="top:95px;">Edit User Profile</div>
    <div class="menu-item" style="top:127px;">Survey Internal Timer</div>
    <div class="menu-item" style="top:158px;">FAQs</div>
    <div class="menu-item" style="top:190px;">About</div>
    <div class="menu-item" style="top:221px;">Exit</div>
  </nav>
</section>
<div class="caption" style="left:556px;top:1072px;">SIDE MENU</div>

</body>
</html>
```